contemporary upscale hair salon

we need a business card design for a modern upscale salon. I would like the card to be vertical, simple, and easy to read. I would like a black matte finish on the info side with white on the back of the card, white lettering with a splash of red incorporated somewhere in there. I also want to incorporate embossing and/or cut out in the letters. The info I would like; Name of the business (Velora Salon) stylist name (Joan) phone number(4096351820) and web address (www.veloraexample.com) I am open to putting shears on the card but without it looking too cheap. Looking for something really modern and edgy. these are just ideas I have, but feel free to show me your creative ideas.
please note: the website is still under construction please do not use any images or colors off the web page. Also i currently do not have a logo, that will be a future project.

Industry/Entity Type

Construction

```html
<!DOCTYPE html>
<html lang="en">
<head>
<meta charset="utf-8">
<title>Velora Salon – Business Card</title>
<link rel="stylesheet" href="https://fonts.googleapis.com/css2?family=Open+Sans:ital,wght@0,300;0,400;0,600;1,700&family=Great+Vibes&family=Dancing+Script:wght@400&display=swap">
<style>
  :root {
    --white: #ffffff;
    --ink: #111111;
    --magenta: #ff12c8;
    --divider: #060606;
    --row-dark: #141414;
    --row-mid: #262626;
    --icon-grey: #7b7b7b;
    --text-light: #dcdcdc;
    --label-grey: #555555;
  }
  * { margin: 0; padding: 0; box-sizing: border-box; }
  html, body { width: 1200px; height: 915px; overflow: hidden; background: var(--white); }
  .sheet { position: relative; width: 1200px; height: 915px; font-family: "Open Sans", sans-serif; }

  /* Back of card */
  .card-back { position: absolute; left: 0; top: 0; width: 548px; height: 915px; background: var(--white); }
  .card-back .wordmark { position: absolute; left: 148px; top: 312px; font-size: 88px; line-height: 84px; }
  .tagline-band { position: absolute; left: 0; top: 565px; width: 548px; height: 126px; background: var(--magenta); }
  .tagline { position: absolute; right: 6px; top: 24px; font-family: "Dancing Script", cursive; font-size: 52px; color: var(--white); white-space: nowrap; }

  .divider { position: absolute; left: 548px; top: 0; width: 104px; height: 915px; background: var(--divider); }

  /* Front of card */
  .card-front { position: absolute; left: 652px; top: 0; width: 548px; height: 915px; background: var(--white); }
  .band { position: absolute; left: 0; width: 548px; background: var(--magenta); }
  .band--top { top: 0; height: 45px; }
  .band--bottom { top: 866px; height: 49px; }
  .card-front .wordmark { position: absolute; left: 126px; top: 100px; font-size: 66px; line-height: 70px; }

  .wordmark { font-weight: 600; color: var(--ink); letter-spacing: -0.5px; }
  .wordmark span { display: block; }

  .stylist { position: absolute; right: 18px; top: 322px; text-align: right; }
  .stylist-name { font-family: "Great Vibes", cursive; font-size: 92px; line-height: 92px; color: var(--magenta); padding-right: 10px; }
  .stylist-role { position: absolute; right: 86px; top: 90px; font-size: 13px; font-weight: 700; font-style: italic; color: var(--label-grey); }

  .contact-row { position: absolute; left: 0; width: 548px; height: 130px; display: flex; align-items: center; color: var(--text-light); }
  .contact-row--address { top: 463px; background: var(--row-dark); }
  .contact-row--phone { top: 593px; background: var(--row-mid); }
  .contact-row--web { top: 723px; height: 130px; background: var(--row-dark); }
  .contact-icon { width: 152px; display: flex; justify-content: center; padding-left: 8px; }
  .contact-icon svg { fill: var(--icon-grey); }
  .contact-text { font-size: 24px; font-weight: 300; line-height: 32px; }
  .contact-row--phone .contact-text { font-size: 17px; line-height: 23px; font-weight: 400; }
</style>
</head>
<body>
<main class="sheet">

  <section class="card-back">
    <h1 class="wordmark"><span>Velora</span><span>Salon</span></h1>
    <div class="tagline-band">
      <p class="tagline">Beauty is everywhere.</p>
    </div>
  </section>

  <div class="divider"></div>

  <section class="card-front">
    <div class="band band--top"></div>

    <h2 class="wordmark"><span>Velora</span><span>Salon</span></h2>

    <div class="stylist">
      <p class="stylist-name">Joan</p>
      <p class="stylist-role">Stylist</p>
    </div>

    <div class="contact-row contact-row--address">
      <div class="contact-icon">
        <svg width="34" height="58" viewBox="0 0 34 58" aria-hidden="true">
          <path d="M17 0C7.6 0 0 7.6 0 17c0 11.5 17 41 17 41s17-29.5 17-41C34 7.6 26.4 0 17 0zm0 24a7 7 0 1 1 0-14 7 7 0 0 1 0 14z"/>
        </svg>
      </div>
      <p class="contact-text">1870 North Alder Lane<br>Brookfield, Texas 70000</p>
    </div>

    <div class="contact-row contact-row--phone">
      <div class="contact-icon">
        <svg width="62" height="52" viewBox="0 0 62 52" aria-hidden="true">
          <path d="M4 4C14-1 48-1 58 4c3 2 4 6 3 10h-13l-2-7H16l-2 7H1C0 10 1 6 4 4z"/>
          <path d="M18 12h26l8 14v24H10V26z"/>
          <g fill="#262626">
            <rect x="22" y="28" width="4" height="4"/><rect x="29" y="28" width="4" height="4"/><rect x="36" y="28" width="4" height="4"/>
            <rect x="22" y="35" width="4" height="4"/><rect x="29" y="35" width="4" height="4"/><rect x="36" y="35" width="4" height="4"/>
            <rect x="22" y="42" width="4" height="4"/><rect x="29" y="42" width="4" height="4"/><rect x="36" y="42" width="4" height="4"/>
          </g>
        </svg>
      </div>
      <p class="contact-text">+000 - 1234 - 5678<br>+000 - 1234 - 5679</p>
    </div>

    <div class="contact-row contact-row--web">
      <div class="contact-icon">
        <svg width="60" height="60" viewBox="0 0 60 60" aria-hidden="true">
          <g fill="none" stroke="var(--icon-grey)" stroke-width="4">
            <circle cx="30" cy="30" r="27"/>
            <ellipse cx="30" cy="30" rx="12" ry="27"/>
            <line x1="30" y1="3" x2="30" y2="57"/>
            <line x1="3" y1="30" x2="57" y2="30"/>
            <path d="M7 16h46M7 44h46"/>
          </g>
        </svg>
      </div>
      <p class="contact-text">info@veloraexample.com<br>www.veloraexample.com</p>
    </div>

    <div class="band band--bottom"></div>
  </section>

</main>
</body>
</html>
```